Interval Timer App

Need to have design for the attached wireframe. Similar app can be found here: https://shop.vantrelapps.net/store/apps/details?id=cc.brimlowe.intervaltimer

```html
<!DOCTYPE html>
<html lang="en">
<head>
<meta charset="utf-8">
<title>Interval Timer App – Screens</title>
<link href="https://fonts.googleapis.com/css2?family=Nunito+Sans:wght@300;400;600;700;800&display=swap" rel="stylesheet">
<style>
:root{
  --bg:#dfdfdf;
  --white:#ffffff;
  --ink:#333333;
  --muted:#9a9a9a;
  --faint:#d6d6d6;
  --blue:#3ea0f0;
  --play-top:#4a9af5;
  --play-bottom:#4b62e0;
  --pink-top:#ec6690;
  --pink-bottom:#dc7a5a;
  --green-top:#28c071;
  --green-bottom:#52b3a2;
  --dark:#333333;
  --dark-label:#7a7a7a;
  --hold-top:#124a2e;
  --hold-bottom:#204a42;
  --done-top:#5bb9f9;
  --done-bottom:#5860e0;
  --icon-green:#2cbf74;
}
*{box-sizing:border-box;margin:0;padding:0}
html,body{width:1200px;height:1038px;overflow:hidden;background:var(--bg)}
body{font-family:"Nunito Sans",sans-serif;color:var(--ink)}
.canvas{position:relative;width:1200px;height:1038px;background:var(--bg)}
.screen{position:absolute;width:185px;height:329px;overflow:hidden;background:var(--white)}
.abs{position:absolute}
.center-x{left:0;right:0;text-align:center}

/* status bar */
.status{position:absolute;top:3px;right:6px;font-size:6.5px;display:flex;align-items:center;gap:2px;color:var(--white)}
.status.on-light{color:#b5b5b5}
.status svg{display:block}

/* settings */
.top-icons{position:absolute;top:20px;right:9px;display:flex;gap:10px}
.field-label{position:absolute;left:0;right:0;text-align:center;font-size:6px;font-weight:700;letter-spacing:.3px}
.stepper{position:absolute;left:16px;width:153px;height:32px;background:var(--white);box-shadow:0 1px 4px rgba(0,0,0,.12);display:flex;align-items:center;font-size:14px;font-weight:400}
.stepper .btn{width:30px;text-align:center;color:var(--blue);font-size:15px;font-weight:300;border-right:1px solid #eee;line-height:18px}
.stepper .btn.plus{border-right:none;border-left:1px solid #eee}
.stepper .value{flex:1;text-align:center}
.stepper.disabled{color:var(--faint)}
.stepper.disabled .btn{color:var(--faint)}
.field-label.disabled{color:var(--faint)}
.play-btn{position:absolute;left:77px;top:282px;width:32px;height:32px;border-radius:50%;background:linear-gradient(var(--play-top),var(--play-bottom));box-shadow:0 2px 6px rgba(60,90,200,.35);display:flex;align-items:center;justify-content:center}
.toolbar{position:absolute;left:0;right:0;bottom:0;height:29px;background:var(--white);box-shadow:0 -1px 4px rgba(0,0,0,.08)}
.tool{position:absolute;top:4px;width:40px;margin-left:-20px;text-align:center;font-size:4px;font-weight:700;color:var(--ink)}
.tool svg{display:block;margin:0 auto 2px}
.toolbar + .play-btn,.play-btn.raised{top:284px;z-index:2}

/* timer */
.pink{background:linear-gradient(var(--pink-top),var(--pink-bottom))}
.green{background:linear-gradient(var(--green-top),var(--green-bottom))}
.dark{background:var(--dark)}
.timer-title{top:59px;font-size:14px;font-weight:400;color:var(--white)}
.ring{position:absolute;left:23px;top:89px;width:140px;height:140px}
.timer-digits{top:141px;font-size:31px;font-weight:600;color:var(--white);letter-spacing:.5px}
.phase{top:226px;font-size:16px;font-weight:800;color:rgba(255,255,255,.35)}
.dark .phase{color:var(--dark-label)}
.pause-btn{position:absolute;left:78px;top:283px;width:30px;height:30px;border-radius:50%;background:var(--white);display:flex;align-items:center;justify-content:center;gap:3px}
.pause-btn i,.ctrl i{display:block;width:1.5px;height:11px;background:var(--ink)}
.pill{position:absolute;left:31px;width:123px;height:30px;border-radius:15px;background:var(--white);font-size:8.5px;font-weight:800;color:var(--ink);display:flex;align-items:center;justify-content:center;letter-spacing:.2px}

/* lock */
.lock-clock{top:48px;font-size:37px;font-weight:300;color:var(--white)}
.lock-band{position:absolute;left:0;right:0;top:119px;height:91px}
.lock-band.green{background:linear-gradient(var(--green-top),var(--green-bottom))}
.lock-band.pink{background:linear-gradient(var(--pink-top),var(--pink-bottom))}
.lock-band.pause{background:linear-gradient(#8c8c8c,#343434)}
.lock-time{top:143px;font-size:24px;font-weight:300;color:var(--white)}
.lock-phase{top:173px;font-size:9px;font-weight:400;color:var(--white)}
.ctrl{position:absolute;top:195px;width:30px;height:30px;border-radius:50%;background:var(--white);display:flex;align-items:center;justify-content:center;gap:3px}
.ctrl .square{width:11px;height:11px;border:1.6px solid var(--ink)}
.slide{top:270px;font-size:9.5px;color:var(--white)}

/* hold overlay */
.hold{background:linear-gradient(var(--hold-top),var(--hold-bottom))}
.hold .faded{opacity:.22}
.pill.play{background:linear-gradient(90deg,var(--play-top),var(--play-bottom));color:var(--white);gap:6px;font-weight:700}

/* all done */
.done{background:linear-gradient(var(--done-top),var(--done-bottom))}
.done-title{top:80px;font-size:16px;font-weight:800;color:var(--white)}
.rate-bar{position:absolute;left:0;right:0;bottom:0;height:29px;border-top:1px solid rgba(255,255,255,.2);display:flex;align-items:center;justify-content:center;gap:3px;font-size:5px;font-weight:700;color:var(--white)}
</style>
</head>
<body>
<div class="canvas">

<!-- ROW 1 -->
<!-- settings plain -->
<section class="screen" style="left:13px;top:13px">
  <div class="status on-light"><svg width="6" height="6"><path d="M0 6H6V0Z" fill="#b5b5b5"/></svg><svg width="3" height="6"><rect width="3" height="6" fill="#b5b5b5"/></svg>50% 10:30</div>
  <div class="top-icons"><svg width="12" height="12" viewBox="0 0 12 12" fill="none" stroke="#555" stroke-width="1"><path d="M2 1V11M6 1V11M10 1V11"/><circle cx="2" cy="7" r="1.3" fill="#fff"/><circle cx="6" cy="4" r="1.3" fill="#fff"/><circle cx="10" cy="8" r="1.3" fill="#fff"/></svg></div>
  <div class="field-label" style="top:76px">SET</div>
  <div class="stepper" style="top:85px"><span class="btn">−</span><span class="value">5</span><span class="btn plus">+</span></div>
  <div class="field-label" style="top:134px">WORK</div>
  <div class="stepper" style="top:142px"><span class="btn">−</span><span class="value">2:30</span><span class="btn plus">+</span></div>
  <div class="field-label" style="top:191px">REST</div>
  <div class="stepper" style="top:200px"><span class="btn">−</span><span class="value">1:30</span><span class="btn plus">+</span></div>
  <div class="play-btn"><svg width="12" height="12" viewBox="0 0 12 12"><path d="M3 1.5L10.5 6L3 10.5Z" fill="none" stroke="#fff" stroke-width="1.4" stroke-linejoin="round"/></svg></div>
</section>

<!-- settings with toolbar, work disabled -->
<section class="screen" style="left:210px;top:13px">
  <div class="status on-light"><svg width="6" height="6"><path d="M0 6H6V0Z" fill="#b5b5b5"/></svg><svg width="3" height="6"><rect width="3" height="6" fill="#b5b5b5"/></svg>50% 10:30</div>
  <div class="top-icons"><svg width="12" height="12" viewBox="0 0 12 12" fill="none" stroke="#555"><path d="M1.5 2H10.5V8.5H5L2.5 10.5V8.5H1.5Z"/><path d="M3.5 4.5H8.5M3.5 6.3H7"/></svg><svg width="12" height="12" viewBox="0 0 12 12" fill="none" stroke="#555"><path d="M2 1V11M6 1V11M10 1V11"/><circle cx="2" cy="7" r="1.3" fill="#fff"/><circle cx="6" cy="4" r="1.3" fill="#fff"/><circle cx="10" cy="8" r="1.3" fill="#fff"/></svg></div>
  <div class="field-label" style="top:76px">SET</div>
  <div class="stepper" style="top:85px"><span class="btn">−</span><span class="value">5</span><span class="btn plus">+</span></div>
  <div class="field-label disabled" style="top:134px">WORK</div>
  <div class="stepper disabled" style="top:142px;box-shadow:none"><span class="btn">−</span><span class="value">2:30</span><span class="btn plus">+</span></div>
  <div class="field-label" style="top:191px">REST</div>
  <div class="stepper" style="top:200px"><span class="btn">−</span><span class="value">1:30</span><span class="btn plus">+</span></div>
  <div class="toolbar">
    <div class="tool" style="left:19px"><svg width="10" height="9" viewBox="0 0 10 9" fill="none" stroke="var(--icon-green)"><path d="M1 3H3L6 1V8L3 6H1Z"/><path d="M7.5 3Q8.5 4.5 7.5 6"/></svg>SOUND</div>
    <div class="tool" style="left:55px"><svg width="12" height="9" viewBox="0 0 12 9" fill="none" stroke="var(--icon-green)"><path d="M1 4.5Q6 -1 11 4.5Q6 10 1 4.5Z"/><circle cx="6" cy="4.5" r="1.6"/></svg>PULSATIONS</div>
    <div class="tool" style="left:130px"><svg width="12" height="9" viewBox="0 0 12 9" fill="none" stroke="#333"><rect x="4" y="1" width="4" height="7"/><path d="M2 2.5V6.5M10 2.5V6.5M0.8 3.5V5.5M11.2 3.5V5.5"/></svg>VIBRATION</div>
    <div class="tool" style="left:166px"><svg width="10" height="9" viewBox="0 0 10 10" fill="none" stroke="#333"><circle cx="5" cy="5.8" r="3.6"/><path d="M5 5.8V3.8M4 1H6"/></svg>FREETIME</div>
  </div>
  <div class="play-btn raised"><svg width="12" height="12" viewBox="0 0 12 12"><path d="M3 1.5L10.5 6L3 10.5Z" fill="none" stroke="#fff" stroke-width="1.4" stroke-linejoin="round"/></svg></div>
</section>

<!-- settings with toolbar -->
<section class="screen" style="left:408px;top:13px">
  <div class="status on-light"><svg width="6" height="6"><path d="M0 6H6V0Z" fill="#b5b5b5"/></svg><svg width="3" height="6"><rect width="3" height="6" fill="#b5b5b5"/></svg>50% 10:30</div>
  <div class="top-icons"><svg width="12" height="12" viewBox="0 0 12 12" fill="none" stroke="#555"><path d="M1.5 2H10.5V8.5H5L2.5 10.5V8.5H1.5Z"/><path d="M3.5 4.5H8.5M3.5 6.3H7"/></svg><svg width="12" height="12" viewBox="0 0 12 12" fill="none" stroke="#555"><path d="M2 1V11M6 1V11M10 1V11"/><circle cx="2" cy="7" r="1.3" fill="#fff"/><circle cx="6" cy="4" r="1.3" fill="#fff"/><circle cx="10" cy="8" r="1.3" fill="#fff"/></svg></div>
  <div class="field-label" style="top:76px">SET</div>
  <div class="stepper" style="top:85px"><span class="btn">−</span><span class="value">5</span><span class="btn plus">+</span></div>
  <div class="field-label" style="top:134px">WORK</div>
  <div class="stepper" style="top:142px"><span class="btn">−</span><span class="value">2:30</span><span class="btn plus">+</span></div>
  <div class="field-label" style="top:191px">REST</div>
  <div class="stepper" style="top:200px"><span class="btn">−</span><span class="value">1:30</span><span class="btn plus">+</span></div>
  <div class="toolbar">
    <div class="tool" style="left:19px"><svg width="10" height="9" viewBox="0 0 10 9" fill="none" stroke="var(--icon-green)"><path d="M1 3H3L6 1V8L3 6H1Z"/><path d="M7.5 3Q8.5 4.5 7.5 6"/></svg>SOUND</div>
    <div class="tool" style="left:55px"><svg width="12" height="9" viewBox="0 0 12 9" fill="none" stroke="var(--icon-green)"><path d="M1 4.5Q6 -1 11 4.5Q6 10 1 4.5Z"/><circle cx="6" cy="4.5" r="1.6"/></svg>PULSATIONS</div>
    <div class="tool" style="left:130px"><svg width="12" height="9" viewBox="0 0 12 9" fill="none" stroke="#333"><rect x="4" y="1" width="4" height="7"/><path d="M2 2.5V6.5M10 2.5V6.5M0.8 3.5V5.5M11.2 3.5V5.5"/></svg>VIBRATION</div>
    <div class="tool" style="left:166px"><svg width="10" height="9" viewBox="0 0 10 10" fill="none" stroke="var(--icon-green)"><circle cx="5" cy="5.8" r="3.6"/><path d="M5 5.8V3.8M4 1H6"/></svg>FREETIME</div>
  </div>
  <div class="play-btn raised"><svg width="12" height="12" viewBox="0 0 12 12"><path d="M3 1.5L10.5 6L3 10.5Z" fill="none" stroke="#fff" stroke-width="1.4" stroke-linejoin="round"/></svg></div>
</section>

<!-- get ready -->
<section class="screen pink" style="left:606px;top:13px">
  <div class="status"><svg width="6" height="6"><path d="M0 6H6V0Z" fill="#fff"/></svg><svg width="3" height="6"><rect width="3" height="6" fill="#fff"/></svg>50% 10:30</div>
  <div class="abs center-x timer-title">REST 5</div>
  <svg class="ring" viewBox="0 0 140 140"><circle cx="70" cy="70" r="62" fill="none" stroke="#fff" stroke-opacity=".6" stroke-width="1"/><circle cx="70" cy="70" r="62" fill="none" stroke="#fff" stroke-width="2.6" stroke-dasharray="368 400" transform="rotate(-90 70 70)"/><circle cx="48.8" cy="11.7" r="3.5" fill="#fff"/></svg>
  <div class="abs center-x timer-digits">00.05</div>
  <div class="abs center-x phase">GET READY</div>
  <div class="pause-btn"><i></i><i></i></div>
</section>

<!-- rest running -->
<section class="screen pink" style="left:804px;top:13px">
  <div class="status"><svg width="6" height="6"><path d="M0 6H6V0Z" fill="#fff"/></svg><svg width="3" height="6"><rect width="3" height="6" fill="#fff"/></svg>50% 10:30</div>
  <div class="abs center-x timer-title">REST 4</div>
  <svg class="ring" viewBox="0 0 140 140"><circle cx="70" cy="70" r="62" fill="none" stroke="#fff" stroke-opacity=".7" stroke-width="1"/><circle cx="70" cy="70" r="62" fill="none" stroke="#fff" stroke-width="2.6" stroke-dasharray="119 400" transform="rotate(-90 70 70)"/><circle cx="128.3" cy="91.2" r="3.5" fill="#fff"/></svg>
  <div class="abs center-x timer-digits">01.05</div>
  <div class="abs center-x phase">REST</div>
  <div class="pause-btn"><i></i><i></i></div>
</section>

<!-- lock rest -->
<section class="screen dark" style="left:1002px;top:13px">
  <div class="status"><svg width="6" height="6"><path d="M0 6H6V0Z" fill="#fff"/></svg><svg width="3" height="6"><rect width="3" height="6" fill="#fff"/></svg>50% 10:30</div>
  <div class="abs center-x lock-clock">13.54</div>
  <div class="lock-band pink"></div>
  <div class="abs center-x lock-time">01.05</div>
  <div class="abs center-x lock-phase">REST 4</div>
  <div class="ctrl" style="left:59px"><i></i><i></i></div>
  <div class="ctrl" style="left:95px"><span class="square"></span></div>
  <div class="abs center-x slide">SLIDE TO UNLOCK</div>
</section>

<!-- ROW 2 -->
<section class="screen dark" style="left:122px;top:354px">
  <div class="status"><svg width="6" height="6"><path d="M0 6H6V0Z" fill="#fff"/></svg><svg width="3" height="6"><rect width="3" height="6" fill="#fff"/></svg>50% 10:30</div>
  <div class="abs center-x timer-title">REST 4</div>
  <svg class="ring" viewBox="0 0 140 140"><circle cx="70" cy="70" r="62" fill="none" stroke="#fff" stroke-width="1"/><circle cx="70" cy="70" r="62" fill="none" stroke="#fff" stroke-width="2.6" stroke-dasharray="352 400" transform="rotate(-90 70 70)"/><circle cx="34.4" cy="19.2" r="3.5" fill="#fff"/></svg>
  <div class="abs center-x timer-digits">00.03</div>
  <div class="abs center-x phase">REST</div>
  <div class="pause-btn"><i></i><i></i></div>
</section>

<section class="screen pink" style="left:312px;top:354px">
  <div class="status"><svg width="6" height="6"><path d="M0 6H6V0Z" fill="#fff"/></svg><svg width="3" height="6"><rect width="3" height="6" fill="#fff"/></svg>50% 10:30</div>
  <div class="abs center-x timer-title">REST 4</div>
  <svg class="ring" viewBox="0 0 140 140"><circle cx="70" cy="70" r="62" fill="none" stroke="#fff" stroke-width="1"/><circle cx="70" cy="70" r="62" fill="none" stroke="#fff" stroke-width="2.6" stroke-dasharray="373 400" transform="rotate(-90 70 70)"/><circle cx="54" cy="10.1" r="3.5" fill="#fff"/></svg>
  <div class="abs center-x timer-digits">00.02</div>
  <div class="abs center-x phase">REST</div>
  <div class="pause-btn"><i></i><i></i></div>
</section>

<section class="screen green" style="left:514px;top:354px">
  <div class="status"><svg width="6" height="6"><path d="M0 6H6V0Z" fill="#fff"/></svg><svg width="3" height="6"><rect width="3" height="6" fill="#fff"/></svg>50% 10:30</div>
  <div class="abs center-x timer-title">WORK 5</div>
  <svg class="ring" viewBox="0 0 140 140"><circle cx="70" cy="70" r="62" fill="none" stroke="#fff" stroke-width="1"/><circle cx="70" cy="8" r="3.5" fill="#fff"/></svg>
  <div class="abs center-x timer-digits">02.30</div>
  <div class="abs center-x phase">WORK</div>
  <div class="pause-btn"><i></i><i></i></div>
</section>

<section class="screen green" style="left:712px;top:354px">
  <div class="status"><svg width="6" height="6"><path d="M0 6H6V0Z" fill="#fff"/></svg><svg width="3" height="6"><rect width="3" height="6" fill="#fff"/></svg>50% 10:30</div>
  <div class="abs center-x timer-title">WORK 5</div>
  <svg class="ring" viewBox="0 0 140 140"><circle cx="70" cy="70" r="62" fill="none" stroke="#fff" stroke-width="2.6"/><circle cx="70" cy="8" r="3.5" fill="#fff"/></svg>
  <div class="abs center-x timer-digits">00.00</div>
  <div class="abs center-x phase">DONE</div>
  <div class="pill" style="top:283px">FINISH A SET</div>
</section>

<section class="screen hold" style="left:910px;top:354px">
  <div class="status" style="opacity:.3"><svg width="6" height="6"><path d="M0 6H6V0Z" fill="#fff"/></svg><svg width="3" height="6"><rect width="3" height="6" fill="#fff"/></svg>50% 10:30</div>
  <div class="faded">
    <div class="abs center-x timer-title">WORK 5</div>
    <svg class="ring" viewBox="0 0 140 140"><circle cx="70" cy="70" r="62" fill="none" stroke="#fff" stroke-width="1.4"/><circle cx="70" cy="8" r="3.5" fill="#fff"/></svg>
    <div class="abs center-x timer-digits">02.30</div>
    <div class="abs center-x phase" style="color:#fff">WORK</div>
  </div>
  <div class="pill" style="top:130px">HOLD TO RESET</div>
  <div class="pill play" style="top:170px"><svg width="10" height="10" viewBox="0 0 12 12"><path d="M3 1.5L10.5 6L3 10.5Z" fill="none" stroke="#fff" stroke-width="1.4" stroke-linejoin="round"/></svg>PLAY</div>
</section>

<!-- ROW 3 -->
<section class="screen dark" style="left:122px;top:697px">
  <div class="status"><svg width="6" height="6"><path d="M0 6H6V0Z" fill="#fff"/></svg><svg width="3" height="6"><rect width="3" height="6" fill="#fff"/></svg>50% 10:30</div>
  <div class="abs center-x timer-title">WORK 5</div>
  <svg class="ring" viewBox="0 0 140 140"><circle cx="70" cy="70" r="62" fill="none" stroke="#fff" stroke-width="1"/><circle cx="70" cy="70" r="62" fill="none" stroke="#fff" stroke-width="2.6" stroke-dasharray="352 400" transform="rotate(-90 70 70)"/><circle cx="34.4" cy="19.2" r="3.5" fill="#fff"/></svg>
  <div class="abs center-x timer-digits">00.03</div>
  <div class="abs center-x phase">WORK</div>
  <div class="pause-btn"><i></i><i></i></div>
</section>

<section class="screen green" style="left:312px;top:697px">
  <div class="status"><svg width="6" height="6"><path d="M0 6H6V0Z" fill="#fff"/></svg><svg width="3" height="6"><rect width="3" height="6" fill="#fff"/></svg>50% 10:30</div>
  <div class="abs center-x timer-title">WORK 5</div>
  <svg class="ring" viewBox="0 0 140 140"><circle cx="70" cy="70" r="62" fill="none" stroke="#fff" stroke-width="1"/><circle cx="70" cy="70" r="62" fill="none" stroke="#fff" stroke-width="2.6" stroke-dasharray="373 400" transform="rotate(-90 70 70)"/><circle cx="54" cy="10.1" r="3.5" fill="#fff"/></svg>
  <div class="abs center-x timer-digits">00.02</div>
  <div class="abs center-x phase">WORK</div>
  <div class="pause-btn"><i></i><i></i></div>
</section>

<section class="screen dark" style="left:514px;top:697px">
  <div class="status"><svg width="6" height="6"><path d="M0 6H6V0Z" fill="#fff"/></svg><svg width="3" height="6"><rect width="3" height="6" fill="#fff"/></svg>50% 10:30</div>
  <div class="abs center-x lock-clock">13.54</div>
  <div class="lock-band green"></div>
  <div class="abs center-x lock-time">00.02</div>
  <div class="abs center-x lock-phase">WORK 5</div>
  <div class="ctrl" style="left:59px"><i></i><i></i></div>
  <div class="ctrl" style="left:95px"><span class="square"></span></div>
  <div class="abs center-x slide">SLIDE TO UNLOCK</div>
</section>

<section class="screen dark" style="left:712px;top:697px">
  <div class="status"><svg width="6" height="6"><path d="M0 6H6V0Z" fill="#fff"/></svg><svg width="3" height="6"><rect width="3" height="6" fill="#fff"/></svg>50% 10:30</div>
  <div class="abs center-x lock-clock">13.54</div>
  <div class="lock-band pause"></div>
  <div class="abs center-x lock-time">00.02</div>
  <div class="abs center-x lock-phase">PAUSE 5</div>
  <div class="ctrl" style="left:59px"><i></i><i></i></div>
  <div class="ctrl" style="left:95px"><span class="square"></span></div>
  <div class="abs center-x slide">SLIDE TO UNLOCK</div>
</section>

<section class="screen done" style="left:910px;top:697px">
  <div class="status"><svg width="6" height="6"><path d="M0 6H6V0Z" fill="#fff"/></svg><svg width="3" height="6"><rect width="3" height="6" fill="#fff"/></svg>50% 10:30</div>
  <div class="abs center-x done-title">ALL DONE!</div>
  <svg class="abs" style="left:56px;top:111px" width="74" height="74" viewBox="0 0 74 74"><circle cx="37" cy="37" r="35.5" fill="none" stroke="#fff" stroke-width="1.2"/><path d="M22 37L32 46L53 28" fill="none" stroke="#fff" stroke-width="2.6" stroke-linecap="round" stroke-linejoin="round"/></svg>
  <div class="pill" style="top:215px">HOLD TO RESET</div>
  <div class="rate-bar"><svg width="7" height="7" viewBox="0 0 10 10"><path d="M5 0.5L6.3 3.6L9.6 3.8L7 6L7.9 9.3L5 7.5L2.1 9.3L3 6L0.4 3.8L3.7 3.6Z" fill="#fff"/></svg>RATE US ON VANTREL SHOP</div>
</section>

</div>
</body>
</html>
```